Brightpath Dentistry - Flyer - Modern & Eye catching campaign flyer

Need front & back side full page flyer designs for both 1) Grand opening 2) On-going campaign.

Attached the new dental office logo.
Attached our other dental clinic flyer designs for content.

Target Market(s)

Cosmetic dentistry

Industry/Entity Type

Health Care

Requirements
Must have
• decent, modern and eye catching marketing flyers.
Nice to have
• - Nice space
• - Highlight phone number
• - Highlight special features like convenient hours, call or text, for all ages, digital facility, etc
Should not have
• - Don't want to fill the flyer with too much wordings
• - Too many colors

```html
<!DOCTYPE html>
<html lang="en">
<head>
<meta charset="utf-8">
<title>Brightpath Dentistry – Flyer</title>
<link href="https://fonts.googleapis.com/css2?family=Open+Sans:wght@600;700&family=Hind:wght@400;500&display=swap" rel="stylesheet">
<style>
  :root{
    --blue:#12a9d8;
    --grey:#6d6e70;
    --ink:#2b2b2b;
    --page:#eef1f3;
    --paper:#ffffff;
    --photo-a:#eef2f3;
    --photo-b:#dfe6e8;
    --map:#e4e5e7;
  }
  *{margin:0;padding:0;box-sizing:border-box}
  html,body{width:1200px;height:1200px;overflow:hidden;background:var(--page)}
  .flyer{position:absolute;left:175px;top:0;width:851px;height:1200px;background:var(--paper);overflow:hidden;font-family:"Hind",sans-serif;color:var(--ink)}
  .header-art{position:absolute;left:0;top:0;width:851px;height:420px}
  .footer-art{position:absolute;left:0;top:1000px;width:851px;height:200px}
  .brand{position:absolute;left:290px;top:150px;display:flex;align-items:center;gap:16px}
  .brand-dot{width:46px;height:46px;border-radius:50%;background:var(--blue)}
  .brand-name{font-family:"Open Sans",sans-serif;font-weight:700;font-size:37px;color:var(--blue);line-height:1;white-space:nowrap}
  .tagline{position:absolute;left:382px;top:202px;font-family:"Open Sans",sans-serif;font-weight:600;font-size:20px;color:var(--grey)}
  .intro{position:absolute;left:30px;top:508px;width:360px}
  .intro-kicker{font-family:"Open Sans",sans-serif;font-weight:700;font-size:30px;color:var(--blue);line-height:1.1;white-space:nowrap}
  .intro-title{font-family:"Open Sans",sans-serif;font-weight:700;font-size:38px;color:var(--grey);line-height:1.15;white-space:nowrap;letter-spacing:-0.5px}
  .intro-copy{position:absolute;left:34px;top:614px;width:330px;font-size:18.5px;line-height:30px;text-align:justify;letter-spacing:.6px}
  .doctor{position:absolute;right:487px;top:782px;font-family:"Open Sans",sans-serif;font-weight:600;font-size:15px;color:var(--blue);display:flex;align-items:center;gap:6px}
  .divider{position:absolute;left:424px;top:559px;width:2px;height:240px;background:#b9babc}
  .services{position:absolute;left:456px;top:508px;width:370px}
  .services-title{font-family:"Open Sans",sans-serif;font-weight:700;font-size:32px;color:var(--blue);line-height:1.3;text-align:center}
  .services-list{list-style:none;margin-top:26px}
  .services-list li{position:relative;padding-left:42px;font-size:18.5px;line-height:23.5px;letter-spacing:.5px;margin-bottom:7px}
  .services-list li::before{content:"-";position:absolute;left:18px;top:6px}
  .cta-label{position:absolute;left:50px;top:870px;font-family:"Open Sans",sans-serif;font-weight:600;font-size:28px;color:var(--grey)}
  .phone{position:absolute;left:44px;top:915px;width:273px;height:50px;border-radius:25px;background:var(--blue);display:flex;align-items:center;color:#fff}
  .phone svg{margin-left:12px}
  .phone-number{margin-left:24px;font-family:"Open Sans",sans-serif;font-weight:600;font-size:31px;letter-spacing:.5px}
  .map-frame{position:absolute;left:407px;top:915px;width:371px;height:228px;border-radius:40px;background:var(--blue)}
  .map{position:absolute;left:14px;top:20px;width:343px;height:190px;border-radius:22px;background:linear-gradient(135deg,#e8e9eb,var(--map) 60%,#d9dbde)}
  .address{position:absolute;left:407px;top:1152px;width:371px;display:flex;align-items:center;justify-content:center;gap:8px;font-family:"Open Sans",sans-serif;font-weight:700;font-size:18px;line-height:1.2;color:var(--blue);white-space:nowrap}
</style>
</head>
<body>
<main class="flyer">
  <svg class="header-art" viewBox="0 0 851 420">
    <defs>
      <linearGradient id="photoTone" x1="0" y1="0" x2="1" y2="1">
        <stop offset="0" stop-color="var(--photo-a)"/>
        <stop offset="1" stop-color="var(--photo-b)"/>
      </linearGradient>
    </defs>
    <path role="img" aria-label="Photo of a smiling dentist in a bright dental treatment room" fill="url(#photoTone)" d="M0,0H851V248C640,330 420,360 250,350C140,344 60,300 0,232Z"/>
    <path fill="var(--blue)" d="M0,168C70,260 170,330 330,350C480,368 640,330 851,240V286C650,370 470,410 320,400C150,388 60,320 0,258Z"/>
    <path fill="var(--blue)" d="M100,300C250,380 430,395 590,380C530,395 420,410 300,400C220,392 160,360 100,300Z"/>
    <path fill="var(--blue)" d="M620,380C720,360 790,330 851,288V300C800,340 720,372 620,380Z"/>
  </svg>

  <div class="brand">
    <span class="brand-dot"></span>
    <span class="brand-name">Brightpath Dentistry</span>
  </div>
  <p class="tagline">Modern Dental Care for All Ages</p>

  <section class="intro">
    <h2 class="intro-kicker">LOOKING FOR DENTIST</h2>
    <h2 class="intro-title">CLOSE TO HOME?</h2>
  </section>
  <p class="intro-copy">Come and See Us for Professional Services and Care. Our dentists and staff are experts in the field of advanced dentistry and will help you achieve your perfect smile.</p>
  <p class="doctor">
    <svg width="16" height="18" viewBox="0 0 16 18" fill="none" stroke="var(--blue)" stroke-width="1.6"><path d="M3,1V6a4,4 0 0 0 8,0V1"/><path d="M7,10v3a3,3 0 0 0 6,0V10"/><circle cx="13" cy="8.5" r="1.6"/></svg>
    Dr. Maren Holloway, D.D.S.
  </p>

  <div class="divider"></div>

  <section class="services">
    <h2 class="services-title">FAMILY &amp; COSMETIC<br>DENTISTRY</h2>
    <ul class="services-list">
      <li>State-Of-The-Art equipment and paperless facility.</li>
      <li>Filled with entertainment devices for patient comfort.</li>
      <li>Same-day appointment for DENTAL EMERGENCIES</li>
      <li>Helping community with routine free kids dental screening.</li>
    </ul>
  </section>

  <svg class="footer-art" viewBox="0 0 851 200" aria-hidden="true">
    <path fill="var(--blue)" d="M0,200C120,150 250,110 420,60L420,80C260,125 130,170 30,200Z"/>
    <path fill="var(--blue)" d="M760,40C800,55 830,75 851,95V110C830,90 800,72 760,58Z"/>
  </svg>

  <p class="cta-label">Call or Text Us Now:</p>
  <div class="phone">
    <svg width="30" height="30" viewBox="0 0 30 30" fill="none" stroke="#fff" stroke-width="1.6"><circle cx="15" cy="15" r="13"/><path d="M11,8c-2,1-2,4 0,8s5,7 7,6l1.5-1.5-2.5-2.5-1.5,1c-1-0.5-3-3-3.5-4.5l1-1.5-2-3.5Z"/></svg>
    <span class="phone-number">555.204.7781</span>
  </div>

  <div class="map-frame">
    <div class="map" role="img" aria-label="Street map showing the clinic location on Linden Pike"></div>
  </div>
  <p class="address">
    <svg width="12" height="17" viewBox="0 0 12 17"><path fill="var(--blue)" d="M6,0a6,6 0 0 1 6,6c0,4-6,11-6,11S0,10 0,6a6,6 0 0 1 6-6Z"/><circle cx="6" cy="6" r="2.2" fill="#fff"/></svg>
    412 Linden Pike, Oakmere PA 19210
  </p>
</main>
</body>
</html>
```